Business Advisory Firm Business Card

A clean, very upscale looking business card. Not crowded.

Please include logo (attached) and:

Danielle R. Kastrup
Four Ashgrove Court
New York, NY 10087
tel: (917) 555-3140
fax: (646) 555-2973
email: dkastrup@silvermerepartners.example
website: www.silvermerepartners.example

Target Market(s)

Business clients. Often real estate development firms, other advisory firms or growing companies that need assistance. I would like a card that looks impressive and confident.

Industry/Entity Type

Business

Colors

Designer to choose colors to be used in the design.

Requirements
Must have
• Impressive and confident. Please include logo.
Should not have
• nothing flashy...

```html
<!DOCTYPE html>
<html lang="en">
<head>
<meta charset="utf-8">
<title>Silvermere Advisory Services – Business Card</title>
<link rel="stylesheet" href="https://fonts.googleapis.com/css2?family=Lato:wght@400;700&display=swap">
<style>
  :root {
    --backdrop: #d6d7d6;
    --paper: #ffffff;
    --green: #9dcb3b;
    --green-pale: #eef5dc;
    --ink: #333333;
    --ink-soft: #4a4a4a;
    --mark-grey: #8c8c8c;
  }
  * { margin: 0; padding: 0; box-sizing: border-box; }
  html, body {
    width: 1200px; height: 1000px; overflow: hidden;
    background: var(--backdrop);
    font-family: "Lato", Arial, sans-serif;
    color: var(--ink);
  }
  .canvas { position: relative; width: 1200px; height: 1000px; }

  .card {
    position: absolute; left: 220px;
    width: 760px; height: 434px;
    background: var(--paper);
    box-shadow: 0 6px 18px rgba(0,0,0,0.18);
    overflow: hidden;
  }
  .card--front { top: 34px; }
  .card--back  { top: 532px; }
  .card__edge {
    position: absolute; left: 0; right: 0; bottom: 0;
    height: 14px; background: var(--green);
  }

  /* front */
  .front__accent {
    position: absolute; right: 70px; top: 40px;
    width: 230px; height: 230px;
    background: var(--green-pale);
  }

  /* brand lockup */
  .brand { position: absolute; display: flex; align-items: center; gap: 22px; }
  .brand__square { width: 74px; height: 74px; background: var(--green); flex: none; }
  .brand__name {
    font-weight: 400; font-size: 30px; line-height: 1.02;
    font-variant: small-caps; letter-spacing: 1px;
    color: var(--ink);
  }
  .card--front .brand { left: 70px; top: 278px; }
  .card--back .brand { left: 56px; top: 300px; }

  /* back */
  .holder__bar {
    position: absolute; left: 0; top: 62px;
    width: 8px; height: 30px; background: var(--green);
  }
  .holder { position: absolute; left: 52px; top: 58px; }
  .holder__name {
    font-weight: 700; font-size: 27px; letter-spacing: 0.5px;
    color: var(--green); text-transform: uppercase;
  }
  .holder__address { font-size: 19px; line-height: 1.3; color: var(--ink-soft); margin-top: 4px; }
  .rule {
    position: absolute; left: 52px; right: 52px; top: 168px;
    height: 2px; background: var(--green);
  }
  .contacts {
    position: absolute; top: 198px; left: 52px; right: 40px;
    display: flex; justify-content: space-between;
    font-size: 18px; line-height: 1.7; color: var(--ink);
  }
  .contacts__label { color: var(--green); font-weight: 700; margin-right: 4px; }
  .contacts__col--web { font-size: 17px; }
</style>
</head>
<body>
<main class="canvas">

  <section class="card card--front" aria-label="Card front">
    <div class="front__accent"></div>
    <div class="brand">
      <span class="brand__square"></span>
      <span class="brand__name">Silvermere<br>Advisory<br>Services, Inc.</span>
    </div>
    <div class="card__edge"></div>
  </section>

  <section class="card card--back" aria-label="Card back">
    <span class="holder__bar"></span>
    <div class="holder">
      <h1 class="holder__name">Danielle R. Kastrup</h1>
      <p class="holder__address">Four Ashgrove Court New York,<br>NY 10087</p>
    </div>
    <div class="rule"></div>
    <div class="contacts">
      <div class="contacts__col">
        <p><span class="contacts__label">P:</span>(917) 555-3140</p>
        <p><span class="contacts__label">F:</span>(646) 555-2973</p>
      </div>
      <div class="contacts__col contacts__col--web">
        <p><span class="contacts__label">E:</span>dkastrup@silvermerepartners.example</p>
        <p><span class="contacts__label">W:</span>www.silvermerepartners.example</p>
      </div>
    </div>
    <div class="brand">
      <span class="brand__square"></span>
      <span class="brand__name">Silvermere<br>Advisory<br>Services, Inc.</span>
    </div>
    <div class="card__edge"></div>
  </section>

</main>
</body>
</html>
```